MOLVT Study flyer

I need help designing a flyer for a research study that will include brain imaging in adolescents. The info is in the attached document. The study is called the Marrowby Orchard Lantern Vesper Trail (MOLVT) study. Ideally this would be returned as a document that I can edit in the future as we will have several new recruitment phases (different age groups, etc. I also would love to have a logo designed as part of this project, but I recognize that might be a separate design request.

```html
<!DOCTYPE html>
<html lang="en">
<head>
<meta charset="utf-8">
<title>MOLVT Study Flyer</title>
<link rel="stylesheet" href="https://fonts.googleapis.com/css2?family=Poppins:wght@400;500;600;700&family=Oswald:wght@600;700&display=swap">
<style>
  :root {
    --blue: #0b63c8;
    --blue-deep: #0857b5;
    --blue-pale: #c9ddf3;
    --ink: #141414;
    --white: #ffffff;
    --photo-warm: #7a5a44;
    --photo-cool: #3f5f8c;
  }
  * { margin: 0; padding: 0; box-sizing: border-box; }
  html, body { width: 860px; height: 1200px; overflow: hidden; background: var(--white); }
  body { font-family: "Poppins", sans-serif; color: var(--ink); }
  .flyer { position: relative; width: 860px; height: 1200px; overflow: hidden; background: var(--white); }
  .shapes { position: absolute; inset: 0; }
  .text { position: absolute; }

  .study-name {
    left: 60px; top: 40px; width: 345px;
    text-align: center; color: var(--white);
    font-size: 22px; line-height: 30px; font-weight: 400;
  }
  .headline {
    left: 20px; top: 135px; width: 404px;
    text-align: center; color: var(--white);
    font-size: 38px; line-height: 52.5px; font-weight: 600;
    text-shadow: 0 2px 6px rgba(0,0,0,.35);
  }
  .about {
    left: 328px; top: 515px; width: 282px;
    text-align: center; color: var(--white);
    font-size: 16.5px; line-height: 24.5px; font-weight: 400;
  }
  .compensation {
    left: 637px; top: 594px; width: 223px; text-align: center; color: var(--white);
    font-family: "Oswald", sans-serif;
  }
  .compensation-label { font-size: 27px; line-height: 40px; font-weight: 600; }
  .compensation-pill {
    display: inline-block; margin-top: 6px; padding: 0 18px;
    height: 40px; line-height: 38px; border-radius: 20px;
    background: var(--blue); font-size: 25px; font-weight: 600;
  }
  .compensation-amount { font-size: 84px; line-height: 96px; font-weight: 700; margin-top: 0; }

  .section-title { font-size: 29px; line-height: 37px; font-weight: 700; color: var(--ink); }
  .involves-title { left: 38px; top: 617px; }
  .eligible-title { left: 467px; top: 821px; }

  .checklist { list-style: none; }
  .checklist li {
    position: relative; padding-left: 33px;
    font-size: 16px; line-height: 20px; font-weight: 500; color: var(--ink);
  }
  .checklist li svg { position: absolute; left: 0; top: 1px; width: 19px; height: 19px; }
  .involves-list { left: 37px; top: 750px; width: 420px; }
  .involves-list li + li { margin-top: 12px; }
  .eligible-list { left: 469px; top: 940px; width: 391px; }
  .eligible-list li + li { margin-top: 16px; }

  .contact-lead {
    left: 29px; top: 1036px; color: var(--white);
    font-size: 27px; line-height: 39px; font-weight: 600;
  }
  .contact-sub {
    left: 29px; top: 1112px; color: var(--white);
    font-size: 20px; line-height: 30px; font-weight: 600;
  }
  .contact-email {
    right: 20px; top: 1134px; color: var(--white);
    font-size: 37px; line-height: 46px; font-weight: 600; letter-spacing: .3px;
    text-shadow: 0 2px 5px rgba(0,0,0,.3);
  }
</style>
</head>
<body>
<main class="flyer">
  <svg class="shapes" width="860" height="1200" viewBox="0 0 860 1200">
    <defs>
      <linearGradient id="heroBlue" x1="0" y1="0" x2="1" y2="1">
        <stop offset="0" stop-color="#1c6fd0"/>
        <stop offset="1" stop-color="#0b5ec4"/>
      </linearGradient>
      <linearGradient id="photoTone" x1="0" y1="0" x2="1" y2="1">
        <stop offset="0" stop-color="#7a5a44"/>
        <stop offset=".55" stop-color="#b0707f"/>
        <stop offset="1" stop-color="#3f5f8c"/>
      </linearGradient>
    </defs>

    <g class="accent-stripes">
      <rect x="759" y="39" width="5" height="110" fill="var(--blue-pale)"/>
      <rect x="774" y="0" width="5" height="156" fill="var(--blue-pale)"/>
      <rect x="787" y="0" width="5" height="176" fill="var(--blue-pale)"/>
      <rect x="830" y="39" width="5" height="157" fill="var(--blue)"/>
      <rect x="842" y="0" width="5" height="202" fill="var(--blue)"/>
      <rect x="855" y="0" width="5" height="210" fill="var(--blue)"/>
    </g>

    <path class="hero-underline" d="M0 498 L140 576 Q184 596 230 574 L300 541 L300 528 L230 561 Q184 583 140 563 L0 485 Z" fill="var(--ink)"/>
    <path class="hero-band" d="M0 0 H648 V300 L560 400 L472 447 L230 561 Q184 583 140 563 L0 485 Z" fill="url(#heroBlue)"/>

    <path class="compensation-panel" d="M860 444 L660 546 Q637 558 637 584 L637 762 Q637 782 656 795 L860 925 Z" fill="var(--ink)"/>

    <g class="photo-frame">
      <polygon points="650,96 864,206 864,417 650,527 436,417 436,206" fill="var(--blue)" stroke="var(--blue)" stroke-width="14" stroke-linejoin="round"/>
      <polygon role="img" aria-label="Photo of a mother and her young daughter sitting on the floor in front of bookshelves, talking"
        points="650,104 858,211 858,413 650,519 442,413 442,211" fill="url(#photoTone)" stroke="url(#photoTone)" stroke-width="10" stroke-linejoin="round"/>
    </g>

    <polygon class="about-hex" points="471,474 616,550 616,695 471,771 326,695 326,550" fill="var(--blue)" stroke="var(--blue)" stroke-width="22" stroke-linejoin="round"/>

    <path class="contact-band" d="M0 1009 Q60 972 111 972 Q140 972 170 988 L389 1103 H860 V1200 H0 Z" fill="var(--blue-deep)"/>
  </svg>

  <p class="text study-name">Marrowby Orchard<br>Lantern Vesper Trail</p>

  <h1 class="text headline">Are you the<br>parent of a child<br>age 10-17?<br>Do they worry<br>or overthink<br>negative<br>emotions ?</h1>

  <p class="text about">Hollenridge<br>University researchers<br>are seeking girls age<br>10-17 for a study about<br>brain activity in emotions<br>and decision-making and<br>how they relate to<br>puberty, anxiety and<br>depression.</p>

  <div class="text compensation">
    <div class="compensation-label">Compensation</div>
    <div class="compensation-pill">up to</div>
    <div class="compensation-amount">$140</div>
  </div>

  <h2 class="text section-title involves-title">Study<br>Participation<br>Involves:</h2>
  <ul class="text checklist involves-list">
    <li><svg viewBox="0 0 20 20"><circle cx="10" cy="10" r="9" fill="var(--blue)"/><path d="M5.8 10.3 L8.6 13 L14.2 7.4" fill="none" stroke="#fff" stroke-width="2" stroke-linecap="round" stroke-linejoin="round"/></svg>One one-hour interview<br>(online or in-person) where your<br>child will discuss their thoughts</li>
    <li><svg viewBox="0 0 20 20"><circle cx="10" cy="10" r="9" fill="var(--blue)"/><path d="M5.8 10.3 L8.6 13 L14.2 7.4" fill="none" stroke="#fff" stroke-width="2" stroke-linecap="round" stroke-linejoin="round"/></svg>Online questionnaires (parent and child)</li>
    <li><svg viewBox="0 0 20 20"><circle cx="10" cy="10" r="9" fill="var(--blue)"/><path d="M5.8 10.3 L8.6 13 L14.2 7.4" fill="none" stroke="#fff" stroke-width="2" stroke-linecap="round" stroke-linejoin="round"/></svg>One two-hour visit where your child will<br>complete an MRI scan, answer questions<br>about their puberty stage, and have a<br>small hair sample taken to study<br>puberty hormones</li>
  </ul>

  <h2 class="text section-title eligible-title">Your Child<br>may be Eligible<br>if they:</h2>
  <ul class="text checklist eligible-list">
    <li><svg viewBox="0 0 20 20"><circle cx="10" cy="10" r="9" fill="var(--blue)"/><path d="M5.8 10.3 L8.6 13 L14.2 7.4" fill="none" stroke="#fff" stroke-width="2" stroke-linecap="round" stroke-linejoin="round"/></svg>Are age 10-17</li>
    <li><svg viewBox="0 0 20 20"><circle cx="10" cy="10" r="9" fill="var(--blue)"/><path d="M5.8 10.3 L8.6 13 L14.2 7.4" fill="none" stroke="#fff" stroke-width="2" stroke-linecap="round" stroke-linejoin="round"/></svg>Tend to worry or overthink negative<br>thoughts</li>
    <li><svg viewBox="0 0 20 20"><circle cx="10" cy="10" r="9" fill="var(--blue)"/><path d="M5.8 10.3 L8.6 13 L14.2 7.4" fill="none" stroke="#fff" stroke-width="2" stroke-linecap="round" stroke-linejoin="round"/></svg>Have not been diagnosed with<br>psychosis, learning problems, or<br>autism</li>
  </ul>

  <p class="text contact-lead">Interested<br>in participating?</p>
  <p class="text contact-sub">Want more information?<br>Please contact us!</p>
  <p class="text contact-email">molvtstudy@brelin.edu</p>
</main>
</body>
</html>
```